Large corporation needs landing page for its employees with emotional and psychological problems

Vision:
Hello, we are a startup and would like to build a landing page and website in the mental health sector for a large corporation. In this site employees with emotional and psychological problems should quickly receive professional psychological support. This support takes the form of internal referrals from employees who are looking for help to qualified therapists, so that help can be provided quickly.
Furthermore, the employees get access to a tool where they can find out about topics in the mind health area and can also get help via webinars and podcasts. The employee should thus be able to take the hurdle to seek help and support in good time.
Therapists for whom the focus is on the urgency of providing quick help and support will work here in cooperation with the respective corporations.
Keywords:
• Help/Support
• overcome inhibitions
• Competent help
• Uncomplicated help
• Permanent access
• protected space
• Recognizing and naming emotional problems and actively tackling them
• get help
• mindfulness
• everyday helper
• Informative
• Anonymous
• compassion
• tolerance
• respect
• Appreciation
• empathy
• mindfulness
• protected space
• To be needed
• Like a lighthouse signal
What we need:
Landingpage
We need a landing page aimed at getting employees to contact psychological help. The call to action is to get in contact via a contact form.
Landing page content
There are several text modules:
• A heading/greeting
• A body of text at the beginning that explains the purpose of the page
• A bulleted text area describing the pain points and the solutions to them
Video:
The heart of the content will be a video explaining the need and inviting them to get in touch.
contact form:
It should be kept simple: first name, last name and email address
Legally required content:
General terms and conditions, data protection and imprint. These are only given as links in the footer.
In parallel, the Corporate Design should be adapted/extended:
Logo:
The font in the logo should be revised. The wings in the background remain.
Please adapt the logo for different uses:
• on a black background
• with transparent background
• favorite icon (browser)
• In square format for social media
Colors:
• develop a color chart based on the colors of the logo.
• please determine 2-3 main colors and the matching variations. I.e. transparent variations or light colors.
Typography:
Determine a decorative font and/or typography for headings and a text font. There should be no more than 3 fonts.
Industry/Entity Type
to recruit therapists as employees
Requirements
Should not have
- please not to playful design or typography - and max. 3 colors

```html
<!DOCTYPE html>
<html lang="en">
<head>
<meta charset="utf-8">
<title>Calmharbor – Support for every employee</title>
<link href="https://fonts.googleapis.com/css2?family=Source+Sans+3:wght@400;600;700&display=swap" rel="stylesheet">
<style>
:root{
  --teal:#0f5561;
  --teal-deep:#0a414b;
  --teal-card:#0c4a55;
  --teal-bright:#1b8f9a;
  --orange:#f0a01c;
  --ink:#1c2326;
  --muted:#6b7478;
  --mist:#e8f0f2;
  --line:#d6dfe2;
  --white:#ffffff;
}
*{box-sizing:border-box;margin:0;padding:0}
html,body{width:1200px;height:4992px;overflow:hidden}
body{font-family:"Source Sans 3",Arial,sans-serif;color:var(--ink);background:var(--white);position:relative}
.abs{position:absolute}
.btn{position:absolute;display:flex;align-items:center;justify-content:center;background:var(--orange);color:var(--white);font-weight:600;font-size:14px;border-radius:4px}
.pill{position:absolute;font-size:11px;padding:3px 10px;border-radius:10px;background:var(--mist);color:var(--teal);font-weight:600}
.pill.dark{background:rgba(255,255,255,.18);color:var(--white)}
.small{font-size:13px;line-height:1.5}
.photo{position:absolute;border-radius:10px;overflow:hidden}

/* header + hero */
.hero-panel{left:500px;top:0;width:700px;height:600px;background:var(--mist)}
.brand{left:48px;top:30px;display:flex;align-items:center;gap:8px;font-size:22px;font-weight:700;color:var(--teal)}
.brand i{width:14px;height:14px;border-radius:50%;background:var(--teal);display:block}
.nav{left:420px;top:36px;display:flex;gap:34px;font-size:14px;color:var(--ink)}
.hero-title{left:100px;top:176px;font-size:42px;font-weight:700;line-height:1.2;width:440px}
.hero-title em{font-style:normal;color:var(--teal-bright)}
.hero-text{left:100px;top:340px;width:330px;color:var(--muted)}
.watch{left:240px;top:408px;display:flex;align-items:center;gap:10px;font-size:14px;font-weight:600}
.watch span{width:30px;height:30px;border-radius:50%;border:2px solid var(--ink);display:flex;align-items:center;justify-content:center}

/* support band */
.band{left:0;width:1200px;background:var(--teal);color:var(--white)}
.band h2{font-size:32px;line-height:1.2;font-weight:700}
.topic{position:absolute;top:900px;width:230px;height:160px;padding:16px 18px}
.topic h3{font-size:18px;margin-bottom:14px}
.topic.active{background:var(--teal-deep)}
.slider{position:absolute;display:flex;align-items:center;gap:12px}
.slider .dot{width:26px;height:26px;border-radius:50%;border:1.5px solid rgba(255,255,255,.6);display:flex;align-items:center;justify-content:center;color:var(--white);font-size:14px}
.slider .dot.on{background:var(--orange);border-color:var(--orange)}
.slider .bar{width:150px;height:2px;background:rgba(255,255,255,.4);position:relative}
.slider .bar::after{content:"";position:absolute;left:0;top:0;width:70px;height:2px;background:var(--white)}

.video{left:168px;top:1180px;width:864px;height:508px;border-radius:14px;background:linear-gradient(135deg,#c9b08a,#8a6f4c 55%,#5d4a33)}
.play{left:560px;top:1394px;width:80px;height:80px;border-radius:50%;background:var(--white);display:flex;align-items:center;justify-content:center}

/* team */
.sec-title{font-size:30px;font-weight:700}
.team-card{top:1928px;width:220px;height:280px}
.team-card .cap{position:absolute;left:16px;bottom:16px;color:var(--white)}
.team-card b{display:block;font-size:17px}
.team-card small{font-size:12px}

.offer{top:2560px;width:192px;height:288px;background:var(--teal-card);border:1px solid rgba(255,255,255,.25);border-radius:6px;padding:16px}
.offer h4{font-size:17px;line-height:1.25;margin-bottom:12px}

/* resources */
.tabs{left:0;width:1200px;top:3240px;display:flex;justify-content:center;gap:14px}
.tabs span{font-size:12px;border:1px solid var(--line);border-radius:12px;padding:3px 14px;color:var(--muted)}
.tabs span.on{border-color:var(--teal);color:var(--teal);font-weight:600}
.article{width:400px;height:104px;display:flex;gap:18px}
.article .thumb{width:160px;height:104px;border-radius:6px;flex:none}
.article h4{font-size:19px;line-height:1.2;margin:8px 0 8px}
.article a{font-size:12px;color:var(--ink);text-decoration:none;border-bottom:1px solid var(--orange)}

/* contact */
.info{top:4096px;display:flex;align-items:center;gap:10px;font-size:13px;color:var(--white)}
.form{left:224px;top:4180px;width:736px;height:400px;background:#eef4f5;border-radius:8px}
.field-label{font-size:12px;color:var(--ink);position:absolute}
.field{position:absolute;width:280px;height:40px;background:var(--mist);border-radius:3px;display:flex;align-items:center;padding-left:12px;gap:12px;font-size:13px;color:var(--ink)}
.field.focus{border:2px solid var(--teal-bright);background:var(--white)}

.footer-links{right:48px;top:4862px;font-size:13px;color:var(--ink)}
.copy{right:48px;top:4904px;font-size:12px;color:var(--muted)}
</style>
</head>
<body>

<!-- header and hero -->
<div class="abs hero-panel"></div>
<div class="abs brand"><i></i>Calmharbor</div>
<nav class="abs nav"><span>Home</span><span>Articles</span><span>Diagnosis</span><span>About</span><span>Contact</span></nav>
<div class="btn" style="left:1020px;top:28px;width:128px;height:34px">Get in Touch</div>
<div class="photo" role="img" aria-label="Therapist in conversation with a client on a sofa" style="left:536px;top:84px;width:624px;height:516px;background:linear-gradient(120deg,#dfe4e2,#bfc7c4 50%,#a4948a)"></div>
<h1 class="abs hero-title">Don't let your <em>struggle</em> become your identity, We got your back</h1>
<p class="abs hero-text small">Reach out when it feels heavy. Our therapists listen without judgement and help you take the first step.</p>
<div class="btn" style="left:100px;top:406px;width:122px;height:34px">Get in Touch</div>
<div class="abs watch">Watch Video <span><svg width="10" height="12"><path d="M1 1 L9 6 L1 11Z" fill="#1c2326"/></svg></span></div>

<!-- support band -->
<section class="abs band" style="top:640px;height:800px">
  <h2 class="abs" style="left:56px;top:80px;width:640px">It's your battle, but you don't need to fight alone, we can help you</h2>
  <div class="btn" style="left:1030px;top:84px;width:112px;height:34px">Learn More</div>
  <p class="abs small" style="left:56px;top:170px;width:560px;opacity:.85">Every struggle deserves a safe place to be heard. Talk to a qualified therapist quickly, privately and with no pressure to explain everything at once.</p>
  <svg class="abs" style="left:0;top:210px" width="1200" height="90" viewBox="0 0 1200 90"><path d="M0 70 C300 10 700 90 1200 20" stroke="rgba(255,255,255,.08)" stroke-width="40" fill="none"/></svg>
</section>
<div class="topic" style="left:40px;color:#fff"><h3>Anxiety</h3><p class="small" style="opacity:.8">Racing thoughts and constant worry can be eased with the right support.</p></div>
<div class="topic active" style="left:276px;color:#fff"><h3>Phobia</h3><p class="small" style="opacity:.85">Intense fears that limit your day can be faced step by step, with a therapist at your side who listens.</p></div>
<div class="topic" style="left:536px;color:#fff"><h3>Addiction</h3><p class="small" style="opacity:.8">Break difficult habits with care, patience and a clear plan.</p></div>
<div class="topic" style="left:796px;color:#fff"><h3>Depression</h3><p class="small" style="opacity:.8">When days feel grey, you do not have to carry it alone.</p></div>
<div class="topic" style="left:1046px;color:#fff"><h3>Anger</h3><p class="small" style="opacity:.8">Understand what sets it off and find calmer ways through.</p></div>
<div class="slider" style="left:920px;top:1080px"><span class="dot">‹</span><span class="bar"></span><span class="dot on">›</span></div>

<div class="abs video" role="img" aria-label="Video still of a therapist speaking to camera"></div>
<div class="abs play"><svg width="26" height="30"><path d="M3 2 L24 15 L3 28Z" fill="#1c2326"/></svg></div>

<!-- team -->
<span class="pill" style="left:56px;top:1800px">Meet Our Team</span>
<h2 class="abs sec-title" style="left:56px;top:1826px">More experts on our team</h2>
<span class="abs" style="left:1050px;top:1840px;font-size:13px">meet all of us →</span>
<div class="abs" style="left:56px;top:1880px;width:1088px;height:1px;background:var(--line)"></div>
<div class="photo team-card" role="img" aria-label="Portrait of therapist Mira Tanaka" style="left:80px;background:linear-gradient(#7c8a84,#3c4a46)"><div class="cap"><b>Mira Tanaka</b><small>read more →</small></div></div>
<div class="photo team-card" role="img" aria-label="Portrait of therapist Owen Hartley" style="left:348px;background:linear-gradient(#7f9a6c,#3e4a38)"><div class="cap"><b>Owen Hartley</b><small>read more →</small></div></div>
<div class="photo team-card" role="img" aria-label="Portrait of therapist Clara Benoit" style="left:612px;background:linear-gradient(#c9c2b6,#5a5248)"><div class="cap"><b>Clara Benoit</b><small>read more →</small></div></div>
<div class="photo team-card" role="img" aria-label="Portrait of therapist Victor Lane" style="left:880px;background:linear-gradient(#c8b9a6,#6a5a4a)"><div class="cap"><b>Victor Lane</b><small>read more →</small></div></div>

<!-- second band -->
<section class="abs band" style="top:2272px;height:696px">
  <h2 class="abs" style="left:508px;top:66px;width:620px">It's your battle, but you don't need to fight alone.</h2>
  <p class="abs small" style="left:508px;top:150px;width:600px;opacity:.85">Our team works with your company so help arrives quickly. Sessions are confidential and shaped around what you need right now.</p>
  <span class="pill dark" style="left:56px;top:208px">Know More</span>
  <h2 class="abs" style="left:56px;top:236px;width:400px">It's your battle, but you don't need to fight alone.</h2>
  <p class="abs small" style="left:56px;top:358px;width:380px;opacity:.85">Naming what you feel is a brave first step. We help you understand it, talk it through and build steady routines for the days ahead.</p>
  <div class="btn" style="left:56px;top:446px;width:112px;height:34px">Learn More</div>
</section>
<div class="abs offer" style="left:508px;color:#fff"><h4>Short-term coaching sessions.</h4><p class="small" style="opacity:.8">Quick, focused talks to help with stress at work and at home, booked within days.</p><p style="font-size:12px;margin-top:12px">read more →</p></div>
<div class="abs offer" style="left:768px;color:#fff"><h4>Private therapy with specialists.</h4><p class="small" style="opacity:.8">Ongoing support from licensed therapists in a protected space that is fully anonymous.</p><p style="font-size:12px;margin-top:12px">read more →</p></div>
<div class="abs offer" style="left:1040px;color:#fff"><h4>Group circles and talks.</h4><p class="small" style="opacity:.8">Share and learn with colleagues facing similar challenges, guided by an expert.</p><p style="font-size:12px;margin-top:12px">read more →</p></div>
<div class="slider" style="left:520px;top:2876px"><span class="dot">‹</span><span class="bar"></span><span class="dot on">›</span></div>

<!-- resources -->
<span class="pill" style="left:520px;top:3088px">Articles, Podcasts &amp; Webinars</span>
<h2 class="abs sec-title" style="left:0;width:1200px;text-align:center;top:3116px">Learn From Our Experts</h2>
<p class="abs small" style="left:400px;width:400px;text-align:center;top:3166px;color:var(--muted)">Short reads, talks and sessions on mindfulness and everyday wellbeing, open to you at any time.</p>
<div class="abs tabs"><span class="on">Articles</span><span>Podcasts</span><span>Videos</span><span>Webinars</span><span>Books</span></div>

<div class="abs article" style="left:196px;top:3290px"><div class="thumb" role="img" aria-label="Two people in a calm discussion" style="background:linear-gradient(135deg,#c9b8a4,#7c6a58)"></div><div><h4>What is the Grey Rock Method and Is It Effective?</h4><a>Learn more →</a></div></div>
<div class="abs article" style="left:604px;top:3290px"><div class="thumb" role="img" aria-label="Parent talking with a child" style="background:linear-gradient(135deg,#8a7a66,#3d342c)"></div><div><h4>Self Punish Often? How to Course Correct without Chastising</h4><a>Learn more →</a></div></div>
<div class="abs article" style="left:196px;top:3410px"><div class="thumb" role="img" aria-label="Person relaxing at a desk" style="background:linear-gradient(135deg,#d8cfc2,#8f8478)"></div><div><h4>Does Success Lead to Happiness?</h4><a>Learn more →</a></div></div>
<div class="abs article" style="left:604px;top:3410px"><div class="thumb" role="img" aria-label="Person looking at a screen in a dim room" style="background:linear-gradient(135deg,#4f6a78,#1f2d36)"></div><div><h4>Can Depression Affect Your Empathy Levels?</h4><a>Learn more →</a></div></div>
<div class="abs article" style="left:196px;top:3530px"><div class="thumb" role="img" aria-label="Friends sharing a moment outdoors" style="background:linear-gradient(135deg,#c7a88a,#6f5842)"></div><div><h4>Can Depression Affect Your Empathy Levels?</h4><a>Learn more →</a></div></div>
<div class="abs article" style="left:604px;top:3530px"><div class="thumb" role="img" aria-label="Colleagues laughing together" style="background:linear-gradient(135deg,#b8c4c8,#5d6a70)"></div><div><h4>Does Success Lead to Happiness?</h4><a>Learn more →</a></div></div>
<div class="btn" style="left:508px;top:3696px;width:184px;height:38px">Discover More Resources</div>

<!-- contact -->
<section class="abs band" style="top:3848px;height:932px">
  <span class="pill dark" style="left:556px;top:66px">Contact Us</span>
  <h2 class="abs" style="left:0;width:1200px;text-align:center;top:96px">Get in touch, we're here for you</h2>
  <p class="abs small" style="left:380px;width:440px;text-align:center;top:146px;opacity:.85">Send a short message and a therapist will reply soon. Everything you share stays private.</p>
</section>
<div class="info" style="left:296px;position:absolute"><svg width="14" height="18"><path d="M7 1a6 6 0 0 0-6 6c0 4 6 10 6 10s6-6 6-10a6 6 0 0 0-6-6z" fill="none" stroke="#fff" stroke-width="1.5"/><circle cx="7" cy="7" r="2" fill="#fff"/></svg>1180 Linden Avenue, NY</div>
<div class="info" style="left:540px;position:absolute"><svg width="16" height="16"><path d="M3 1l3 3-2 2c1 2 3 4 5 5l2-2 3 3-2 3C7 15 1 9 0 4z" fill="#fff"/></svg>555-014-2290</div>
<div class="info" style="left:752px;top:4082px;position:absolute;background:var(--teal-deep);padding:12px 16px;border-radius:4px"><svg width="16" height="12"><rect x=".75" y=".75" width="14.5" height="10.5" fill="none" stroke="#fff" stroke-width="1.5"/><path d="M1 1l7 6 7-6" fill="none" stroke="#fff" stroke-width="1.5"/></svg>hello@calmharbor.org</div>

<div class="abs form">
  <span class="field-label" style="left:40px;top:30px">Your Name</span>
  <div class="field" style="left:40px;top:50px"><svg width="12" height="14"><circle cx="6" cy="4" r="3" fill="#1b8f9a"/><path d="M0 14a6 5 0 0 1 12 0z" fill="#1b8f9a"/></svg>Logan Johns</div>
  <span class="field-label" style="left:40px;top:110px">Email</span>
  <div class="field focus" style="left:40px;top:130px"><svg width="14" height="10"><rect width="14" height="10" fill="#1b8f9a"/><path d="M0 0l7 5 7-5" fill="none" stroke="#fff"/></svg><span style="width:1px;height:16px;background:var(--ink)"></span></div>
  <span class="field-label" style="left:40px;top:190px">Phone</span>
  <div class="field" style="left:40px;top:210px"><svg width="10" height="16"><rect x="1" y="1" width="8" height="14" rx="2" fill="none" stroke="#1b8f9a" stroke-width="1.5"/></svg></div>
  <span class="field-label" style="left:384px;top:30px">Message</span>
  <div class="abs" style="left:384px;top:50px;width:312px;height:200px;background:var(--mist);border-radius:3px"></div>
  <div class="btn" style="left:308px;top:320px;width:120px;height:34px">Send Message</div>
</div>

<!-- footer -->
<div class="abs brand" style="top:4870px"><i></i>Calmharbor</div>
<div class="abs" style="left:48px;top:4910px;width:1104px;height:1px;background:var(--line)"></div>
<div class="abs footer-links">Data protection and Imprint &nbsp;•&nbsp; Terms and conditions</div>
<div class="abs copy" style="top:4924px">Copyright © 2023 Calmharbor</div>

</body>
</html>
```